Buch-/eBook-Cover für Autobiografie
Das Disign von dem Cover hat mir auf Anhieb sehr gut gefallen. Das hat gleich "ins schwarze" getroffen. Die Kommunikation war effizient und zielgerichtet
Zielgruppe
Ich bin eine Privatperson und habe im Laufe der letzten Jahre mein Autobiografie geschrieben. Besser gesagt ist es ein autobiografischer Roman geworden. Ich plane dieses Buch meiner Frau und meinen Söhnen und deren Familien zu schenken. Darüber hinaus ist es aber auch geplant das Buch bei Bravoria zu veröffentlichen.
Aufgabenstellung
Auf dem Cover sollte neben meinem Namen Rupert(a) Hallmann natürlich auch der Titel von dem Buch stehen. Ich habe dem Buch den Titel gegeben: 'Das Licht am Ufer'. Auf dem Backcover hatte ich mir eine kurze zusammenfassung vorgestellt, die ich auch beifüge. Ich hatte geplant, das sowohl auf dem Cover, wie auch auf dem Backcover Bilder von mir (u.a. als Baby) mit gestaltet werden. Aber das ist nur so eine Idee, ich bin da für Vorschläge offen
Das Design darf nicht zu überladen sein.

```html
<!DOCTYPE html>
<html lang="de">
<head>
<meta charset="utf-8">
<title>Das Licht am Ufer – Buchumschlag</title>
<link rel="stylesheet" href="https://fonts.googleapis.com/css2?family=EB+Garamond:ital,wght@0,400;0,500;1,400&display=swap">
<style>
  :root {
    --paper: #f3ead8;
    --paper-light: #f7f0e2;
    --paper-shade: #ebe0c9;
    --ink: #1f2a33;
    --ink-soft: #2b2a26;
    --line: #2c3a48;
    --arrow: #1f5fa8;
    --frame: #fbf7ee;
  }
  * { margin: 0; padding: 0; box-sizing: border-box; }
  html, body { width: 1200px; height: 800px; overflow: hidden; background: var(--paper); }
  .cover-spread {
    position: relative;
    width: 1200px; height: 800px;
    font-family: "EB Garamond", Georgia, serif;
    color: var(--ink);
    background: linear-gradient(180deg, var(--paper-light), var(--paper) 60%, var(--paper-shade));
    overflow: hidden;
  }
  .back-cover, .front-cover { position: absolute; top: 0; height: 800px; }
  .back-cover { left: 0; width: 600px; }
  .front-cover { left: 600px; width: 600px; }
  .spine-fold {
    position: absolute; left: 598px; top: 0; width: 4px; height: 800px;
    background: linear-gradient(90deg, rgba(0,0,0,0), rgba(120,100,70,0.18), rgba(0,0,0,0));
  }
  .back-rule {
    position: absolute; left: 0; top: 393px; width: 598px; height: 1px;
    background: linear-gradient(90deg, var(--line) 0 264px, transparent 264px 268px, var(--line) 268px 498px, transparent 498px 502px, var(--line) 502px);
    opacity: 0.75;
  }
  .blurb {
    position: absolute; left: 85px; top: 478px; width: 400px;
    text-align: center; font-size: 17px; line-height: 1; color: var(--ink-soft);
  }
  .blurb p { margin-bottom: 14px; }
  .blurb p.gap { margin-top: 7px; }
  .author {
    position: absolute; left: 0; width: 550px; top: 50px;
    text-align: center; font-size: 30px; font-weight: 400; letter-spacing: 0.5px;
  }
  .title {
    position: absolute; left: 0; width: 550px; top: 138px;
    text-align: center; font-weight: 400; line-height: 0.9;
  }
  .title .title-main { display: block; font-size: 76px; }
  .title .title-sub { display: block; font-size: 74px; font-style: italic; }
  .genre {
    position: absolute; left: 0; width: 554px; top: 710px;
    text-align: center; font-size: 19px; color: var(--ink-soft);
  }
  .snapshot {
    position: absolute; background: var(--frame); padding: 6px;
    border-radius: 5px; box-shadow: 0 3px 8px rgba(60,45,20,0.28);
  }
  .snapshot .photo { width: 100%; height: 100%; border-radius: 2px; }
  .snapshot.baby { left: 640px; top: 408px; width: 136px; height: 150px; transform: rotate(-3deg); }
  .snapshot.baby .photo { background: linear-gradient(160deg, #d9d2c6, #c9b49c 55%, #e7dccb); }
  .snapshot.child { left: 795px; top: 374px; width: 129px; height: 142px; transform: rotate(-1deg); }
  .snapshot.child .photo { background: linear-gradient(170deg, #5f7a4a, #8c8a62 50%, #c5b8a4); }
  .snapshot.adult { left: 971px; top: 333px; width: 141px; height: 166px; transform: rotate(1.5deg); }
  .snapshot.adult .photo { background: linear-gradient(160deg, #7a6a55, #a88566 45%, #34465c); }
  .timeline { position: absolute; left: 0; top: 0; width: 1200px; height: 800px; pointer-events: none; }
</style>
</head>
<body>
<div class="cover-spread">
  <section class="back-cover">
    <div class="back-rule"></div>
    <div class="blurb">
      <p>Erinnerungen, die verblassen.</p>
      <p>Momente, die bleiben.</p>
      <p class="gap">Die Reise durch ein Leben –</p>
      <p>von den Anfängen bis zum Hier und Jetzt.</p>
    </div>
  </section>

  <div class="spine-fold"></div>

  <section class="front-cover">
    <div class="author">Rupert(a) Hallmann</div>
    <h1 class="title">
      <span class="title-main">Das Licht</span>
      <span class="title-sub">am Ufer</span>
    </h1>
    <div class="genre">Ein autobiografischer Roman</div>
  </section>

  <div class="snapshot baby"><div class="photo" role="img" aria-label="Foto des Autors als lachendes Baby"></div></div>
  <div class="snapshot child"><div class="photo" role="img" aria-label="Foto des Autors als Kind im gestreiften Shirt"></div></div>
  <div class="snapshot adult"><div class="photo" role="img" aria-label="Foto des Autors als erwachsener Mann"></div></div>

  <svg class="timeline" viewBox="0 0 1200 800" aria-hidden="true">
    <defs>
      <linearGradient id="timeline-stroke" x1="469" y1="555" x2="1184" y2="384" gradientUnits="userSpaceOnUse">
        <stop offset="0" stop-color="#2c3a48" stop-opacity="0"/>
        <stop offset="0.3" stop-color="#2c3a48" stop-opacity="0.9"/>
        <stop offset="0.8" stop-color="#23486f"/>
        <stop offset="1" stop-color="#1f5fa8"/>
      </linearGradient>
    </defs>
    <line x1="469" y1="555" x2="1185" y2="384" stroke="url(#timeline-stroke)" stroke-width="2"/>
    <path d="M1162 386 L1138 380 L1142 389 L1136 398 Z" fill="var(--arrow)"/>
  </svg>
</div>
</body>
</html>
```